Corwenna Foundation is a new grant making charity set up in the UK.

Having got a logo, we now need a website to go with it. We have worked out the text which people are going to need in order to then apply for grants. But having found out what we require they will probably need to go away and think about it.
We have to be careful of what images we use. So I have uploaded some images that we like. We are also going to be adding more pages almost immediately so need to think about the images for these.
I know basic wordpress so I will be able to add new pages/make alterations in future.
Updates
The website does need to be coded in Wordpress so that I can maintain it afterwards.
Corwenna
Brief changed to provide more money and we have also provided more possible pictures. And generally more explanation.
Target Market(s)
departments in universities, other charities doing work on relief of pain, people working in health service departments
Industry/Entity Type
Health Charity
Coding
Coded - Design and coding required
Number of Pages Required
4 page
Look and feel
Each slider illustrates characteristics of the customer's brand and the style your logo design should communicate.

```html
<!DOCTYPE html>
<html lang="en">
<head>
<meta charset="utf-8">
<title>Corwenna Foundation</title>
<link rel="stylesheet" href="https://fonts.googleapis.com/css2?family=Montserrat:wght@500;600;700;800&family=Raleway:wght@400;500;600&display=swap">
<style>
:root{
  --blue:#0a63b8;
  --blue-dark:#0a3f86;
  --navy:#1b3563;
  --orange:#e8821f;
  --green:#14a37c;
  --teal:#18a9b6;
  --ink:#333a45;
  --muted:#6b7280;
  --line:#c9d3de;
  --white:#ffffff;
  --panel:#f3f4f6;
}
*{margin:0;padding:0;box-sizing:border-box}
html,body{width:1200px;height:2832px;overflow:hidden;background:var(--white)}
body{position:relative;font-family:"Raleway",Arial,sans-serif;color:var(--ink)}
.abs{position:absolute}
.heading{font-family:"Montserrat",Arial,sans-serif;font-weight:700;letter-spacing:.5px}

/* header */
.site-header{left:0;top:0;width:1200px;height:80px;background:var(--white);border-bottom:1px solid #e5e7eb}
.brand{display:flex;align-items:center;gap:9px;font-family:"Montserrat",Arial,sans-serif;font-weight:700;color:var(--blue);font-size:19px;letter-spacing:.5px}
.brand-square{width:30px;height:30px;border:3px solid var(--blue)}
.site-header .brand{left:132px;top:22px}
.main-nav{top:22px;font-family:"Montserrat",Arial,sans-serif;font-size:14px;font-weight:600;color:#4b5563;letter-spacing:.4px}
.main-nav.active{color:var(--blue)}
.main-nav.active::after{content:"";position:absolute;left:-4px;right:-4px;top:31px;height:3px;background:var(--blue)}

/* hero */
.hero{left:0;top:80px;width:1200px;height:636px;background:radial-gradient(circle at 68% 40%,#6d8fe0 0%,#1d4fa8 22%,#0d2a66 55%,#061737 100%)}
.hero-frame{left:136px;top:252px;width:431px;height:249px;border:4px solid var(--white);text-align:center;color:var(--white)}
.hero-frame h1{font-family:"Montserrat",Arial,sans-serif;font-weight:800;font-size:46px;line-height:49px;margin-top:30px;letter-spacing:1px}
.hero-frame p{font-family:"Montserrat",Arial,sans-serif;font-weight:700;font-size:20px;line-height:27px;margin-top:10px;letter-spacing:.5px}
.hero-cta{left:280px;top:478px;width:153px;height:43px;border-radius:22px;background:var(--blue);color:var(--white);font-family:"Montserrat",Arial,sans-serif;font-weight:700;font-size:13px;display:flex;align-items:center;justify-content:center;box-shadow:0 0 0 9px var(--blue-dark) inset,0 0 0 0 transparent}
.hero-cta{box-shadow:none}
.slider-arrow{top:346px;width:40px;height:40px;border-radius:50%;background:var(--white);display:flex;align-items:center;justify-content:center}

/* features */
.features{left:0;top:716px;width:1200px;height:400px;background:linear-gradient(#f1f1f2,#ffffff)}
.card{top:832px;width:303px;height:242px;border:2px solid var(--line);background:var(--white);text-align:center}
.card.featured{background:linear-gradient(160deg,#1469c4,#0a55ad);border-color:#0a5ab0;color:var(--white)}
.card h3{font-family:"Montserrat",Arial,sans-serif;font-weight:700;font-size:17px;margin-top:70px;letter-spacing:.6px;color:#2b2f36}
.card.featured h3{color:var(--white)}
.card p{font-size:11.5px;line-height:20px;color:var(--muted);margin:8px auto 0;width:240px}
.card.featured p{color:#dbe8fb}
.pill{display:inline-flex;align-items:center;justify-content:center;width:132px;height:37px;border-radius:19px;border:2px solid;font-family:"Montserrat",Arial,sans-serif;font-weight:700;font-size:11.5px;margin-top:18px}
.icon-tile{top:781px;width:98px;height:88px;background:var(--white);padding:5px;border:1px solid var(--line)}
.icon-tile div{width:100%;height:100%;display:flex;align-items:center;justify-content:center}

/* about */
.about-visual{left:128px;top:1165px;width:424px;height:424px;border-radius:50%;border:2px solid #9fd8c5;padding:10px}
.about-visual div{width:100%;height:100%;border-radius:50%;border:2px solid #7fb4e0;background:radial-gradient(circle at 50% 70%,#c3423a 0%,#a84a3a 30%,#2f4a78 60%,#ffffff 61%)}
.about-title{left:616px;top:1220px;font-family:"Montserrat",Arial,sans-serif;font-weight:800;font-size:29px;line-height:35px;letter-spacing:1px}
.about-title .t1{color:var(--blue)}
.about-title .t2{color:var(--green)}
.about-rule{left:618px;top:1300px;width:60px;height:3px;background:var(--blue)}
.about-copy{left:616px;top:1320px;width:440px;font-size:16.5px;line-height:28px;color:#3a3f47}
.about-copy p+p{margin-top:18px}
.about-cta{left:611px;top:1481px;width:152px;height:42px;border:2px solid var(--blue);color:var(--blue);border-radius:22px;font-family:"Montserrat",Arial,sans-serif;font-weight:700;font-size:12.5px;display:flex;align-items:center;justify-content:center}

/* grants */
.grants{left:0;top:1658px;width:1200px;height:534px;background:radial-gradient(circle at 78% 45%,#3e8fe0 0%,#1660c2 30%,#0d3f8e 60%,#08234f 100%)}
.grants-title{left:134px;top:1780px;color:var(--white);font-family:"Montserrat",Arial,sans-serif;font-weight:800;font-size:31px;letter-spacing:1px}
.grants-rule{left:135px;top:1824px;width:60px;height:3px;background:var(--white)}
.grants-copy{left:134px;top:1850px;width:400px;color:var(--white);font-size:14px;line-height:19px}
.grants-copy p+p{margin-top:16px}
.grants-cta{left:134px;top:2007px;width:154px;height:43px;border-radius:22px;background:var(--white);color:var(--navy);font-family:"Montserrat",Arial,sans-serif;font-weight:700;font-size:13px;display:flex;align-items:center;justify-content:center}

/* contact */
.contact{left:0;top:2192px;width:1200px;height:560px;background:linear-gradient(180deg,#1aa9b8,#109bb0 60%,#0c8ea6)}
.contact-title{left:0;top:2252px;width:1200px;text-align:center;color:var(--white);font-family:"Montserrat",Arial,sans-serif;font-weight:800;font-size:28px;letter-spacing:1.5px}
.contact-rule{left:569px;top:2298px;width:68px;height:3px;background:var(--white)}
.field{left:198px;width:401px;height:47px;background:#f7f8fb;display:flex;align-items:center;gap:10px;padding-left:20px;font-size:13px;color:#4b5563}
.field-message{left:608px;top:2335px;width:399px;height:160px;background:#f7f8fb;padding:16px 22px;font-size:13px;color:#4b5563}
.submit{left:521px;top:2525px;width:172px;height:44px;border-radius:22px;background:var(--navy);color:var(--white);font-family:"Montserrat",Arial,sans-serif;font-weight:700;font-size:15px;letter-spacing:1px;display:flex;align-items:center;justify-content:center}

/* footer */
.footer-curve{left:0;top:2600px;width:1200px;height:232px}
.site-footer .brand{left:478px;top:2664px;font-size:22px}
.footer-nav{top:2751px;font-family:"Montserrat",Arial,sans-serif;font-weight:600;font-size:14.5px;color:#2b2f36;letter-spacing:.5px}
.copyright{left:0;top:2787px;width:1200px;text-align:center;font-size:11.5px;color:var(--navy)}
</style>
</head>
<body>

<header class="abs site-header">
  <div class="abs brand"><span class="brand-square"></span>CORWENNA FOUNDATION</div>
  <nav>
    <a class="abs main-nav active" style="left:540px">HOME</a>
    <a class="abs main-nav" style="left:655px">ABOUT US</a>
    <a class="abs main-nav" style="left:804px">GRANTS</a>
    <a class="abs main-nav" style="left:938px">CONTACT US</a>
  </nav>
</header>

<section class="abs hero" role="img" aria-label="Photograph of a glowing blue neuron with orange light points"></section>
<div class="abs hero-frame">
  <h1>CORWENNA<br>FOUNDATION</h1>
  <p>WE REDUCE THE SUFFERING<br>CAUSED BY CHRONIC PAIN.</p>
</div>
<a class="abs hero-cta">CONTACT US</a>
<span class="abs slider-arrow" style="left:28px"><svg width="14" height="14" viewBox="0 0 14 14"><path d="M9 2 4 7l5 5" fill="none" stroke="#1b2233" stroke-width="2.6"/></svg></span>
<span class="abs slider-arrow" style="left:1132px"><svg width="14" height="14" viewBox="0 0 14 14"><path d="M5 2l5 5-5 5" fill="none" stroke="#1b2233" stroke-width="2.6"/></svg></span>

<section class="abs features"></section>
<article class="abs card" style="left:143px">
  <h3>WHY WE ARE</h3>
  <p>Lorem ipsum dolor sit amet, consectetur adipiscing elit, sed do eiusmod tempor incididunt ut labore et dolore</p>
  <a class="pill" style="color:var(--orange)">LEARN MORE</a>
</article>
<article class="abs card featured" style="left:453px">
  <h3>OUR GRANTS</h3>
  <p>Lorem ipsum dolor sit amet, consectetur adipiscing elit, sed do eiusmod tempor incididunt ut labore et dolore</p>
  <a class="pill" style="color:var(--white);border-color:var(--white)">LEARN MORE</a>
</article>
<article class="abs card" style="left:768px">
  <h3>OUR MISSION</h3>
  <p>Lorem ipsum dolor sit amet, consectetur adipiscing elit, sed do eiusmod tempor incididunt ut labore et dolore</p>
  <a class="pill" style="color:var(--green)">LEARN MORE</a>
</article>
<div class="abs icon-tile" style="left:249px;border-color:var(--orange)"><div style="background:var(--orange)"><svg width="44" height="40" viewBox="0 0 44 40" fill="none" stroke="#fff" stroke-width="2"><path d="M22 6c-4-4-12-2-13 4-5 1-6 8-2 11-2 5 3 10 8 8 2 4 7 4 7 0V6zM22 6c4-4 12-2 13 4 5 1 6 8 2 11 2 5-3 10-8 8-2 4-7 4-7 0"/></svg></div></div>
<div class="abs icon-tile" style="left:555px;border-color:var(--blue)"><div style="background:var(--blue)"><svg width="46" height="46" viewBox="0 0 46 46" fill="none" stroke="#fff" stroke-width="2"><path d="M10 38c8 0 14-4 14-12s-6-10-6-16M18 10l-6-4M18 14l-8 2M24 26c6 0 10 4 14 10"/><circle cx="32" cy="10" r="2"/><circle cx="36" cy="18" r="1.5"/></svg></div></div>
<div class="abs icon-tile" style="left:871px;border-color:var(--green)"><div style="background:var(--green)"><svg width="48" height="48" viewBox="0 0 48 48" fill="none" stroke="#fff" stroke-width="2.2"><circle cx="22" cy="26" r="16"/><circle cx="22" cy="26" r="9"/><circle cx="22" cy="26" r="2.5"/><path d="M22 26 40 8M34 8h6v6"/></svg></div></div>

<div class="abs about-visual"><div role="img" aria-label="Illustration of a crowd of people in warm and blue tones"></div></div>
<h2 class="abs about-title"><span class="t1">ABOUT CORWENNA</span><br><span class="t2">FOUNDATION</span></h2>
<span class="abs about-rule"></span>
<div class="abs about-copy">
  <p>Corwenna Foundation is a grant making charity set up in the UK in 2021. The main aim of Corwenna Foundation is to reduce the suffering caused by chronic pain.</p>
  <p>Charity registration number 1187654.</p>
</div>
<a class="abs about-cta">LEARN MORE</a>

<section class="abs grants" role="img" aria-label="Photograph of connected blue neurons"></section>
<h2 class="abs grants-title">CORWENNA GRANTS</h2>
<span class="abs grants-rule"></span>
<div class="abs grants-copy">
  <p>Grants will almost entirely be provided for research or education into pain management, or the prevention of pain.</p>
  <p>The trustees will also be providing grants to a number of other charities or to areas with which they have had a long term association such as HIV/AIDS and TB. There is no application procedure for these other areas</p>
</div>
<a class="abs grants-cta">LEARN MORE</a>

<section class="abs contact"></section>
<h2 class="abs contact-title">CONTACT CORWENNA</h2>
<span class="abs contact-rule"></span>
<label class="abs field" style="top:2335px"><svg width="14" height="14" viewBox="0 0 14 14" fill="none" stroke="#4b5563" stroke-width="1.3"><circle cx="7" cy="4.5" r="3"/><path d="M1.5 13c0-3 2.5-5 5.5-5s5.5 2 5.5 5"/></svg>Name</label>
<label class="abs field" style="top:2390px"><svg width="16" height="12" viewBox="0 0 16 12"><rect width="16" height="12" fill="#4b5563"/><path d="M0 0l8 7 8-7" fill="none" stroke="#f7f8fb" stroke-width="1.3"/></svg>E-mail address</label>
<label class="abs field" style="top:2446px"><svg width="14" height="14" viewBox="0 0 14 14"><path d="M3 1l2.5 3-1.5 1.5c1 2 2.5 3.5 4.5 4.5L10 8.5 13 11l-2 2C6 13 1 8 1 3z" fill="#4b5563"/></svg>Phone</label>
<div class="abs field-message">Message</div>
<a class="abs submit">SUBMIT</a>

<svg class="abs footer-curve" viewBox="0 0 1200 232" preserveAspectRatio="none">
  <path d="M0 110Q600-10 1200 110V232H0z" fill="#ffffff"/>
  <path d="M0 110Q600 10 1140 88" fill="none" stroke="#2a7fd0" stroke-width="3"/>
  <path d="M160 70Q600 20 1100 80" fill="none" stroke="#14a37c" stroke-width="3"/>
</svg>
<footer class="site-footer">
  <div class="abs brand"><span class="brand-square"></span>CORWENNA FOUNDATION</div>
  <a class="abs footer-nav" style="left:318px">HOME</a>
  <a class="abs footer-nav" style="left:440px">ABOUT US</a>
  <a class="abs footer-nav" style="left:598px">GRANTS</a>
  <a class="abs footer-nav" style="left:740px">CONTACT US</a>
  <p class="abs copyright">Copyright © 2021 Corwenna Foundation &nbsp;|&nbsp; All Rights Reserved</p>
</footer>

</body>
</html>
```